Missing Kids Car Doantion Website Design

Please create a new one page website design.

Current site: http://autosforyouth.net/

New WEBSITE address is: VansForLostYouth.org

Use these sites for an idea of what I am looking for. I like these sites best: tiresforsoldiers.org and autosforsoldiers.org

Coding

Coded - Design and coding required

Number of Pages Required

1 page

```html
<!DOCTYPE html>
<html lang="en">
<head>
<meta charset="utf-8">
<title>Autos for Youth – Give Your Wheels</title>
<link rel="stylesheet" href="https://fonts.googleapis.com/css2?family=Lato:wght@400;700;900&family=Open+Sans:wght@400;600;700&display=swap">
<style>
:root{
  --blue:#1f66d9;
  --blue-dark:#1a4f9c;
  --ink:#1c1c1c;
  --text:#555b63;
  --muted:#7a8088;
  --panel:rgba(16,22,30,.78);
  --panel-head:#2c5877;
  --pale:#eef3f9;
  --line:#c9ced5;
  --white:#fff;
  --band:#2d4f6e;
}
*{box-sizing:border-box;margin:0;padding:0}
html,body{width:1200px;height:2711px;overflow:hidden}
body{position:relative;font-family:"Open Sans",Arial,sans-serif;color:var(--text);background:var(--white)}

/* header */
.site-header{position:absolute;left:0;top:0;width:1200px;height:103px;background:var(--white)}
.brand{position:absolute;left:99px;top:14px}
.brand-name{font-family:"Lato",Arial,sans-serif;font-weight:900;font-size:34px;color:var(--blue);line-height:1;white-space:nowrap}
.brand-tag{font-family:"Lato",Arial,sans-serif;font-size:17px;color:#444;margin-top:10px}
.main-nav{position:absolute;right:98px;top:40px;display:flex;gap:30px;align-items:center;font-family:"Lato",Arial,sans-serif;font-weight:700;font-size:16px;color:var(--ink);white-space:nowrap}
.main-nav .active{color:var(--blue)}

/* hero */
.hero{position:absolute;left:0;top:103px;width:1200px;height:529px;overflow:hidden}
.hero-photo{position:absolute;inset:0;background:linear-gradient(90deg,#4a7f8f 0%,#7ea3a8 18%,#d98a55 38%,#e9b07a 50%,#3a3f48 70%,#1d2128 100%)}
.hero-arrow{position:absolute;top:262px}
.hero-title{position:absolute;left:99px;top:322px;font-family:"Lato",Arial,sans-serif;font-weight:700;font-size:38px;letter-spacing:-.8px;color:var(--white);white-space:nowrap;line-height:1.2}
.hero-sub{position:absolute;left:101px;top:374px;font-family:"Open Sans",Arial,sans-serif;font-size:20px;color:var(--white);white-space:nowrap}
.btn-ghost{position:absolute;top:428px;height:52px;border:2px solid var(--white);border-radius:26px;color:var(--white);font-family:"Lato",Arial,sans-serif;font-weight:700;font-size:16px;display:flex;align-items:center;justify-content:center}

.donate-panel{position:absolute;left:669px;top:0;width:431px;height:529px;background:var(--panel)}
.donate-head{height:78px;background:var(--panel-head);color:var(--white);font-family:"Lato",Arial,sans-serif;font-weight:900;font-size:23px;text-align:center;line-height:27px;padding-top:12px}
.donate-lead{position:absolute;left:0;width:100%;top:114px;text-align:center;color:var(--white);font-size:15px}
.donate-check{position:absolute;left:127px;top:149px;color:var(--white);font-size:15px;display:flex;align-items:center;gap:9px}
.donate-check span.box{width:13px;height:13px;border:1.5px solid var(--white);border-radius:2px}
.field{position:absolute;width:184px}
.field label{display:block;color:var(--white);font-size:12.5px;margin-bottom:6px;white-space:nowrap}
.field .input{height:36px;background:var(--white);position:relative}
.field .select::after{content:"";position:absolute;right:0;top:0;width:40px;height:36px;background:#e4e4e4}
.field .select::before{content:"";position:absolute;right:15px;top:15px;border:6px solid transparent;border-top-color:#888;z-index:1}
.btn-next{position:absolute;left:139px;top:437px;width:152px;height:51px;border-radius:26px;background:var(--blue);color:var(--white);font-family:"Lato",Arial,sans-serif;font-weight:700;font-size:17px;display:flex;align-items:center;justify-content:center}

/* welcome */
.welcome-title{position:absolute;left:99px;top:708px;font-family:"Lato",Arial,sans-serif;font-weight:700;font-size:35px;line-height:43px;color:var(--ink)}
.welcome-copy{position:absolute;left:99px;top:812px;width:490px;font-size:13.5px;line-height:27px;color:var(--text)}
.btn-solid{position:absolute;background:var(--blue-dark);color:var(--white);border-radius:22px;font-family:"Lato",Arial,sans-serif;font-weight:700;font-size:14px;display:flex;align-items:center;justify-content:center}
.video-frame{position:absolute;left:634px;top:718px;width:467px;height:311px;border:1px solid #d5d5d5;background:var(--white);padding:4px}
.video-still{width:100%;height:100%;background:linear-gradient(160deg,#6f8a4c 0%,#9aa57a 35%,#c8c0ac 60%,#b6aa94 100%);position:relative}
.play{position:absolute;left:50%;top:50%;width:54px;height:54px;margin:-27px 0 0 -27px;border-radius:50%;background:rgba(0,0,0,.75);border:2px solid var(--white)}
.play::after{content:"";position:absolute;left:21px;top:15px;border:11px solid transparent;border-left:16px solid var(--white);border-right:0}

/* why */
.why{position:absolute;left:0;top:1151px;width:1200px;height:636px;background:var(--pale)}
.section-title{position:absolute;left:0;width:100%;text-align:center;font-family:"Lato",Arial,sans-serif;font-weight:700;font-size:34px;color:var(--ink)}
.feature{position:absolute;top:193px;width:316px;height:255px;background:var(--white);border:1.5px solid #9aa0a8;text-align:center}
.feature-icon{position:absolute;left:50%;top:-52px;margin-left:-52px;width:104px;height:104px;border-radius:50%;background:var(--white);border:1.5px solid #9aa0a8;display:flex;align-items:center;justify-content:center}
.feature h3{margin-top:72px;font-family:"Open Sans",Arial,sans-serif;font-weight:600;font-size:22px;line-height:30px;color:var(--ink)}
.feature p{margin:14px auto 0;width:250px;font-size:13.5px;line-height:26px;color:var(--text)}

/* stats */
.stats{position:absolute;left:0;top:1787px;width:1200px;height:540px;overflow:hidden}
.stats-photo{position:absolute;inset:0;background:linear-gradient(180deg,#2f5374 0%,#3f6686 45%,#2b4a68 100%)}
.stats-lead{position:absolute;left:180px;width:840px;top:56px;text-align:center;color:var(--white);font-size:18px;line-height:34px;font-weight:600}
.stat{position:absolute;top:174px;width:330px;text-align:center;color:var(--white)}
.stat-ring{width:156px;height:156px;margin:0 auto;border:4px solid var(--white);border-radius:50%;display:flex;align-items:center;justify-content:center}
.stat-num{font-family:"Lato",Arial,sans-serif;font-weight:700;font-size:36px;margin-top:24px}
.stat-label{font-size:18px;line-height:27px;margin-top:6px}

/* footer */
.site-footer{position:absolute;left:0;top:2327px;width:1200px;height:384px;background:var(--white)}
.foot-brand{position:absolute;left:90px;top:148px;font-family:"Lato",Arial,sans-serif;font-weight:900;font-size:31px;color:var(--blue);white-space:nowrap}
.foot-col{position:absolute;top:86px}
.foot-col h4{font-family:"Open Sans",Arial,sans-serif;font-weight:600;font-size:19px;color:var(--ink);margin-bottom:20px;white-space:nowrap}
.foot-links li{list-style:none;font-size:12.5px;line-height:25px;color:#333}
.foot-news p{font-size:12.5px;line-height:21px;color:#333;width:230px}
.email-field{margin-top:14px;width:253px;border-bottom:1px solid #999;padding:0 0 7px 14px;font-size:12px;color:#999}
.btn-sub{margin-top:16px;width:106px;height:33px;border-radius:17px;background:var(--blue);color:var(--white);font-size:12px;font-weight:600;display:flex;align-items:center;justify-content:center}
.contact li{list-style:none;display:flex;gap:20px;font-size:12.5px;line-height:18px;color:#333;margin-bottom:18px}
.contact svg{flex:none;margin-top:2px}
.foot-rule{position:absolute;left:99px;top:302px;width:1002px;height:1px;background:var(--line)}
.copyright{position:absolute;left:99px;top:328px;font-size:12px;color:#333}
.social{position:absolute;right:99px;top:324px;display:flex;gap:8px}
.social span{width:26px;height:26px;border:1.5px solid var(--blue);border-radius:50%}
</style>
</head>
<body>

<header class="site-header">
  <div class="brand">
    <div class="brand-name">Give Your Wheels!</div>
    <div class="brand-tag">Help Find Missing Kids</div>
  </div>
  <nav class="main-nav">
    <span class="active">HOME</span>
    <span>ABOUT SEEK THE YOUNG</span>
    <span>MISSING KIDS</span>
    <span>CONTACT</span>
    <span>FAQ</span>
    <svg width="16" height="16" viewBox="0 0 16 16"><circle cx="6.5" cy="6.5" r="5" fill="none" stroke="#1c1c1c" stroke-width="2.2"/><line x1="10.2" y1="10.2" x2="14.5" y2="14.5" stroke="#1c1c1c" stroke-width="2.6" stroke-linecap="round"/></svg>
  </nav>
</header>

<section class="hero">
  <div class="hero-photo" role="img" aria-label="Photo of a young girl with short hair looking down, beside a car at sunset"></div>
  <svg class="hero-arrow" style="left:14px" width="14" height="24" viewBox="0 0 14 24"><polyline points="12,2 2,12 12,22" fill="none" stroke="#fff" stroke-width="2.5" opacity=".8"/></svg>
  <svg class="hero-arrow" style="right:14px" width="14" height="24" viewBox="0 0 14 24"><polyline points="2,2 12,12 2,22" fill="none" stroke="#fff" stroke-width="2.5" opacity=".8"/></svg>
  <h1 class="hero-title">DONATE YOUR CAR OR BOAT</h1>
  <p class="hero-sub">Every 10 minutes, there's an attempt to abduct a child.</p>
  <div class="btn-ghost" style="left:99px;width:152px">MISSING KIDS</div>
  <div class="btn-ghost" style="left:262px;width:152px">LEARN MORE</div>

  <form class="donate-panel">
    <div class="donate-head">2-STEP DONATION - MADE<br>QUICK &amp; EASY</div>
    <p class="donate-lead">Fill out the form &amp; help protect the future of children.</p>
    <div class="donate-check"><span class="box"></span>Donate a boat instead</div>
    <div class="field" style="left:25px;top:206px"><label>Year *</label><div class="input"></div></div>
    <div class="field" style="left:220px;top:206px"><label>Make *</label><div class="input"></div></div>
    <div class="field" style="left:25px;top:275px"><label>Model *</label><div class="input"></div></div>
    <div class="field" style="left:220px;top:275px"><label>Does it run? *</label><div class="input select"></div></div>
    <div class="field" style="left:25px;top:347px"><label>Do you have the title? *</label><div class="input select"></div></div>
    <div class="field" style="left:220px;top:347px"><label>Any major damage?</label><div class="input select"></div></div>
    <div class="btn-next">NEXT STEP</div>
  </form>
</section>

<section class="welcome">
  <h2 class="welcome-title">WELCOME TO<br>AUTOS FOR YOUTH</h2>
  <p class="welcome-copy">Seek the Young is a non-profit corporation dedicated to the recovery of missing children and to the prevention of the abuse and endangerment of children. Seek the Young assists families searching for missing children by helping them to access local and federal law enforcement, advising them on the appropriate legal documents,...</p>
  <div class="btn-solid" style="left:99px;top:986px;width:123px;height:42px">READ MORE</div>
  <div class="video-frame">
    <div class="video-still" role="img" aria-label="Video still of a child in a yellow dress holding balloons at a playground">
      <span class="play"></span>
    </div>
  </div>
</section>

<section class="why">
  <h2 class="section-title" style="top:52px">WHY CHOOSE US</h2>

  <div class="feature" style="left:99px">
    <div class="feature-icon">
      <svg width="44" height="44" viewBox="0 0 44 44"><polygon points="40,4 4,20 18,24 22,40" fill="#1f66d9"/><polyline points="40,4 18,24" stroke="#fff" stroke-width="2" fill="none"/></svg>
    </div>
    <h3>Fast Free Pickup -<br>24hr Response</h3>
    <p>Seek the Young is the coordinating agency for the Child Abduction Task Force, &nbsp;a multi-agency team</p>
  </div>

  <div class="feature" style="left:442px">
    <div class="feature-icon">
      <svg width="40" height="44" viewBox="0 0 40 44"><rect x="3" y="2" width="34" height="40" rx="3" fill="none" stroke="#1f66d9" stroke-width="3"/><rect x="9" y="8" width="22" height="8" fill="#1f66d9"/><g fill="#1f66d9"><rect x="9" y="21" width="5" height="4"/><rect x="17.5" y="21" width="5" height="4"/><rect x="26" y="21" width="5" height="4"/><rect x="9" y="28" width="5" height="4"/><rect x="17.5" y="28" width="5" height="4"/><rect x="26" y="28" width="5" height="4"/><rect x="9" y="35" width="5" height="4"/><rect x="17.5" y="35" width="5" height="4"/><rect x="26" y="35" width="5" height="4"/></g></svg>
    </div>
    <h3>Tax Deduction -<br>Easy To Do!</h3>
    <p>Seek the Young is the coordinating agency for the Child Abduction Task Force, &nbsp;a multi-agency team</p>
  </div>

  <div class="feature" style="left:785px">
    <div class="feature-icon">
      <svg width="48" height="40" viewBox="0 0 48 40"><path d="M10 16 L14 5 H34 L38 16 H44 V32 H4 V16 Z" fill="#1f66d9"/><path d="M15 15 L18 9 H30 L33 15 Z" fill="#fff"/><circle cx="12" cy="24" r="3" fill="#fff"/><circle cx="36" cy="24" r="3" fill="#fff"/><rect x="6" y="31" width="8" height="7" rx="1.5" fill="#1f66d9"/><rect x="34" y="31" width="8" height="7" rx="1.5" fill="#1f66d9"/></svg>
    </div>
    <h3>No Emission<br>Test Required</h3>
    <p>Seek the Young is the coordinating agency for the Child Abduction Task Force, &nbsp;a multi-agency team</p>
  </div>

  <div class="btn-solid" style="left:515px;top:488px;width:170px;height:51px;background:var(--blue);border-radius:26px;font-size:16px">DONATE NOW!</div>
</section>

<section class="stats">
  <div class="stats-photo" role="img" aria-label="Dim blue-toned photo of a boat moored at a lakeside dock"></div>
  <p class="stats-lead">According to the Department of Justice, each year, there are approximately 94,000 missing children, 90,000 runaways, 300 stranger abductions, and 981 family abductions.</p>

  <div class="stat" style="left:106px">
    <div class="stat-ring">
      <svg width="72" height="56" viewBox="0 0 72 56"><g fill="#fff"><circle cx="36" cy="13" r="9"/><path d="M20 50 C20 34 26 26 36 26 C46 26 52 34 52 50 Z"/><circle cx="16" cy="17" r="7"/><path d="M2 46 C2 34 7 28 16 28 C19 28 21 29 22 30 C18 35 17 40 17 46 Z"/><circle cx="56" cy="17" r="7"/><path d="M70 46 C70 34 65 28 56 28 C53 28 51 29 50 30 C54 35 55 40 55 46 Z"/></g></svg>
    </div>
    <div class="stat-num">800,000</div>
    <div class="stat-label">Children are reported<br>missing a year</div>
  </div>

  <div class="stat" style="left:433px">
    <div class="stat-ring">
      <svg width="60" height="60" viewBox="0 0 60 60"><circle cx="24" cy="24" r="17" fill="none" stroke="#fff" stroke-width="7"/><line x1="37" y1="37" x2="54" y2="54" stroke="#fff" stroke-width="9" stroke-linecap="round"/></svg>
    </div>
    <div class="stat-num">751,000</div>
    <div class="stat-label">Children have seen the Seek the<br>Young program</div>
  </div>

  <div class="stat" style="left:767px">
    <div class="stat-ring">
      <svg width="60" height="62" viewBox="0 0 60 62"><g fill="none" stroke="#fff" stroke-width="3.5" stroke-linejoin="round"><path d="M6 10 H24 L32 18 V44 H6 Z"/><path d="M24 10 V18 H32"/><path d="M28 20 H46 L54 28 V56 H28 Z" fill="#3a5f80"/><path d="M46 20 V28 H54"/></g></svg>
    </div>
    <div class="stat-num">400+</div>
    <div class="stat-label">Open missing<br>children cases</div>
  </div>
</section>

<footer class="site-footer">
  <div class="foot-brand">Give Your Wheels!</div>

  <div class="foot-col" style="left:425px">
    <h4>Quick Links</h4>
    <ul class="foot-links">
      <li>Help</li><li>FAQ</li><li>Support</li><li>Sitemap</li><li>Terms Of Use</li><li>Privacy Statement</li>
    </ul>
  </div>

  <div class="foot-col foot-news" style="left:598px">
    <h4>Newsletter Subscription</h4>
    <p>Register your Email Address to get information about us</p>
    <div class="email-field">Email Address</div>
    <div class="btn-sub">SUBSCRIBE</div>
  </div>

  <div class="foot-col" style="left:907px">
    <h4>Contact Us</h4>
    <ul class="contact">
      <li><svg width="12" height="16" viewBox="0 0 12 16"><path d="M6 0 C9.5 0 12 2.6 12 6 C12 10 6 16 6 16 C6 16 0 10 0 6 C0 2.6 2.5 0 6 0 Z" fill="#1f66d9"/><circle cx="6" cy="6" r="2.2" fill="#fff"/></svg><span>Level 12, 48 Harbour Lane<br>Leeds, UK</span></li>
      <li><svg width="14" height="14" viewBox="0 0 14 14"><path d="M3 0 L5.5 3.5 L4 5.5 C5 7.5 6.5 9 8.5 10 L10.5 8.5 L14 11 L12 14 C5.5 13.5 0.5 8.5 0 2 Z" fill="#1f66d9"/></svg><span>1 800 555 0142</span></li>
      <li><svg width="14" height="14" viewBox="0 0 14 14"><rect x="0" y="4" width="14" height="10" rx="1" fill="#1f66d9"/><rect x="3" y="0" width="8" height="5" fill="#1f66d9"/><rect x="3" y="7" width="8" height="1.5" fill="#fff"/><rect x="3" y="10" width="8" height="1.5" fill="#fff"/></svg><span>1 800 555 0178</span></li>
      <li><svg width="14" height="11" viewBox="0 0 14 11"><rect width="14" height="11" rx="1" fill="#1f66d9"/><polyline points="0.5,1 7,6 13.5,1" fill="none" stroke="#fff" stroke-width="1.3"/></svg><span>info@autosforyouth.net</span></li>
    </ul>
  </div>

  <div class="foot-rule"></div>
  <p class="copyright">Copyrights © 2017, Autos for Youth. All rights reserved.</p>
  <div class="social"><span></span><span></span><span></span><span></span></div>
</footer>

</body>
</html>
```